Coaching landingpage/salespage need a layout

Hi!
We are two people from Sweden looking for help to design our coaching landingpage/salespage.

What about:
We need a nice modern timeless appealing Photoshop layout (landingpage) for our coaching page where we coach people to “how to get a richer lifestyle”.

Style of page:
We want the site to reflect seriousness but still harmonic. We would like somewhat colorful and (but not too crazy). After all, we are coaching about investments and private economy.
Responsive layout – consider stacking order when scaling down window width. Fullpage-design where content areas are 960 grid/max-width.

----------------------------------------------------------------------------
Content on page:
*Headersection – Logo and header image with the two coaches together and space for later on adding a video.

*On the landingpage the customers can read up on what we mean by a richer lifestyle (use dummy text). We show our Vardagskartan (= Lifestyle matrix) and a little description about that. If the customers want to know more, they can click "read more (or a symbolic icon that relates to read more)" to expand a hidden div (section) where they can read more about Vardagskartan. They can also minimize the section.

*3-4 Unique selling points “Four reasons why choose coaching” with nice designed number-icons and some place for text.

*The customer should also be able to read something about what happens during a typical coaching session, some bullets that summarize it (use dummy text) and a couple of headlines, maybe 3 or 4 (about what they need to prepare for themselves .eg Talkio, headset/microphone etc).

*Offer/product section: A section where the customer can see what services we provide, choose product and click order. When customer click order they will arrive to an order-page (this one you don’t have to design) .
Our products are as followed: Bronze (single coaching session), Silver (small-package), Gold (large-package). Use provided graphics for these products.

*Testimonials section. Currently we have 2 good testimonials, but only with text no portrait picture.

Testimonial1: “Uppiggande och inspirerande! Kommer med enkla vardagstips såväl som svårare tips. Ett roligt sätt att få en spark i baken, så att ekonomi-energin bibehålls! Tack för ett bra samtal!" - Annelie Brunstedt

Testimonial2: "Värdefullast för mig var kunskapen om alternativa investeringssställen som inte är börs eller eget ägande." - Josefin Harkeby

*Section with portraits and info about the coaches (currently 2 coaches, but in future will be several, so a design-section that’s lets us add more coaches).

*Footer-section
------------------------------------------------------------------------

Colors:
Use Vardagskartan (attached file) as colorinspiration. Doesn’t have to be exactly those colors, you can use similar colors if it is more pleasing to the eye and you can also use complementary colors.

Currently we have tried of our own but don't really nail it with any apealing design. This is what we have done so far but we want to replace it with your more professional design:

https://www.kelbrostudio.se/full/Page/coaching13
-------------------------------------------------------------

SUMMARIZE of the above design-description:

* Our logo (attached psd-file with smart-object. You can try different colors with color-overlay)

*Apealing headerimage with portrait (attached file "big_portrait")

*Introduction text (use dummy text about 100 words)

*Text about Vardagskartan (use dummy text about 200 words)

*Vardagskartan (attached psd-file with smart-object)

*What we are covering during a coaching session (dummy text about 200 words and about 5 or 6 bullets)

*3-4 Unique Selling Points with stylish number icons (not 2 small) and some text.
*Our offers Bronze, Silver, Gold (attached pictures)
*Testimonials
*Picture & info about coaches (attached pictures, choose whichever suits you)
*Footer

Please comment if there are questions.

Reagards Henrik @ Kelbro Studio

Target Market(s)

People who want to learn how to create a richer lifestyle which involves more freedom and a better well-being

Number of Pages Required

1 page

Font styles to use
Sans Serif
Other font styles liked:
• Roboto

Requirements
Should not have
• A cheezy unmodern landingpage with lots of texts and 10 sign-up buttons.
• This page is not a site about capturing emails and building lists by provide a "best-guide-for-something". It´s about getting people to book and pay for one or more coaching-sessions.

```html
<!DOCTYPE html>
<html lang="en">
<head>
<meta charset="utf-8">
<title>Kelbro Studio – Lifestyle Coaching</title>
<link href="https://fonts.googleapis.com/css2?family=Open+Sans:ital,wght@0,400;0,600;0,700;1,400&display=swap" rel="stylesheet">
<style>
:root{
  --orange:#fbb03b;
  --orange-dark:#e8962a;
  --ink:#222;
  --text:#666;
  --blue:#29a8e0;
  --grey-bg:#f2f2f2;
  --card-bg:#f7f7f7;
  --dark:#1d1d1d;
  --footer:#333;
  --footer-deep:#252525;
  --bronze:#d98a48;
  --bronze-band:#b8692c;
  --silver:#d8d8d8;
  --silver-band:#9d9d9d;
  --gold:#eec24a;
  --gold-band:#cf9e1f;
  --white:#fff;
}
*{box-sizing:border-box;margin:0;padding:0}
html,body{width:1200px;height:3947px;overflow:hidden}
body{font-family:"Open Sans",Arial,sans-serif;color:var(--text);background:var(--white);font-size:13px;line-height:1.65}
.wrap{width:784px;margin:0 auto;position:relative}
section,header,footer{position:relative;overflow:hidden}
h2.section-title{font-size:24px;font-weight:600;color:var(--ink);text-align:center;line-height:1.3}
h2.section-title::after{content:"";display:block;width:34px;height:3px;background:var(--orange);margin:10px auto 0}
.btn-outline{display:inline-block;border:2px solid var(--orange);color:var(--orange);font-weight:600;font-size:13px;padding:8px 26px;text-decoration:none}

/* nav */
.topbar{height:79px;background:var(--orange)}
.topbar .wrap{display:flex;align-items:center;justify-content:space-between;height:79px}
.brand{display:flex;align-items:center;gap:10px;color:var(--white);font-size:22px;font-weight:400;letter-spacing:3px;text-transform:uppercase}
.brand .mark{width:22px;height:22px;background:var(--white)}
.main-nav{display:flex;gap:22px;height:79px;align-items:stretch}
.main-nav a{color:var(--white);font-size:13px;font-weight:600;text-decoration:none;display:flex;align-items:center;position:relative}
.main-nav a.active{color:var(--ink)}
.main-nav a.active::after{content:"";position:absolute;left:-6px;right:-6px;bottom:0;height:5px;background:var(--ink)}

/* hero */
.hero-photo{height:329px;background:radial-gradient(ellipse at 50% 45%,#55704a 0%,#2e3f2a 45%,#141a12 100%)}
.hero-band{height:113px;background:var(--dark)}
.hero-band .wrap{display:flex;align-items:center;justify-content:space-between;height:113px}
.hero-band h1{color:var(--white);font-size:25px;font-weight:600;line-height:1.3;max-width:600px}
.hero-band .btn-outline{padding:11px 46px;color:var(--orange)}

/* intro */
.intro{height:326px;text-align:center;padding-top:118px}
.intro p{width:560px;margin:18px auto 26px;font-size:12.5px}

/* lifestyle */
.lifestyle{height:408px;background:var(--grey-bg)}
.lifestyle .wrap{display:flex;gap:76px;padding-top:21px}
.matrix-art{width:332px;height:370px;background:linear-gradient(135deg,#7bbf3a 0%,#f3a03a 40%,#8c6d52 65%,#3aa870 100%);opacity:.85;border-radius:4px}
.lifestyle-copy{padding-top:60px;width:376px}
.lifestyle-copy h3{font-size:22px;font-weight:600;color:var(--ink);margin-bottom:16px}
.lifestyle-copy p{font-size:12.5px;margin-bottom:12px}
.lifestyle-copy .btn-outline{margin-top:8px}

/* why */
.why{height:363px;padding-top:62px}
.usp-row{display:flex;gap:13px;margin-top:32px}
.usp{width:186px;height:218px;background:var(--card-bg);text-align:center}
.usp .label{height:40px;line-height:40px;font-size:14px;font-weight:600;color:var(--blue);background:#eeeeee}
.usp.featured .label{background:var(--orange);color:var(--white)}
.usp .num{width:82px;height:82px;border-radius:50%;background:var(--blue);color:var(--white);font-size:34px;line-height:82px;margin:14px auto 18px;border:4px solid var(--white);box-shadow:0 0 0 1px #ddd}
.usp.featured .num{background:#8d7b6e}
.usp p{font-size:11.5px;line-height:1.5;padding:0 16px}

/* covering */
.covering{height:527px;padding-top:50px}
.covering h4{font-size:15px;font-weight:700;color:var(--ink);margin:34px 0 10px}
.covering p{font-size:12.5px}
.covering .lead{font-weight:700;color:#444;margin-top:14px}
.ticks{display:grid;grid-template-columns:1fr 1fr;gap:4px 40px;margin-top:10px;list-style:none}
.ticks li{display:flex;gap:8px;align-items:center;font-size:12.5px}
.ticks svg{flex:none}
.divider{height:1px;background:#ddd;margin:24px 0 6px}
.prep{display:grid;grid-template-columns:1fr 1fr;gap:40px}
.prep h4{margin-top:16px}

/* packages */
.packages{height:605px;background:linear-gradient(160deg,#2c333d 0%,#454c56 55%,#2a2f36 100%);padding-top:62px;color:var(--white);text-align:center}
.packages h2.section-title{color:var(--white)}
.packages .intro-text{width:560px;margin:14px auto 0;font-size:12.5px;color:#e5e5e5}
.package-row{display:flex;gap:20px;margin-top:70px}
.package{width:248px;height:300px;position:relative;padding-top:102px}
.package .medal{position:absolute;left:50%;top:-46px;transform:translateX(-50%);width:118px;height:118px;border-radius:50%;border:6px solid var(--white)}
.package .band{height:40px;line-height:40px;font-size:15px;font-weight:700;color:var(--white)}
.package .details{font-size:13px;line-height:1.6;color:var(--ink);margin-top:30px}
.package .btn{display:inline-block;margin-top:22px;padding:6px 18px;font-size:12px;color:var(--white);text-decoration:none}
.bronze{background:var(--bronze)}.bronze .band{background:var(--bronze-band)}.bronze .medal{background:radial-gradient(circle,#e0955a,#8f4f1f)}.bronze .btn{background:#8e4d1c}
.silver{background:var(--silver)}.silver .band{background:var(--silver-band)}.silver .medal{background:radial-gradient(circle,#eeeeee,#8a8a8a)}.silver .btn{background:#7a7a7a}
.gold{background:var(--gold)}.gold .band{background:var(--gold-band)}.gold .medal{background:radial-gradient(circle,#ffe27a,#c8901a)}.gold .btn{background:#a8790f}

/* testimonials */
.testimonials{height:355px;padding-top:58px;text-align:center}
.quote-mark{font-size:64px;line-height:1;color:var(--blue);font-family:Georgia,serif;margin-top:24px;height:46px}
.testimonials blockquote{width:560px;margin:16px auto 16px;font-style:italic;font-size:13px;line-height:1.55}
.testimonials cite{font-style:normal;font-weight:700;color:var(--ink);font-size:14px}
.dots{display:flex;gap:6px;justify-content:center;margin-top:18px}
.dots span{width:8px;height:8px;border-radius:50%;background:#ccc}
.dots span.on{background:var(--blue)}

/* coaches */
.coaches{height:527px;background:var(--grey-bg);padding-top:74px}
.coach-row{display:flex;gap:42px;margin-top:42px}
.coach{width:371px;height:332px;background:#e6e6e6;text-align:center;padding-top:118px;position:relative}
.coach .portrait{position:absolute;left:50%;top:-14px;transform:translateX(-50%);width:118px;height:118px;border-radius:50%;border:5px solid var(--white)}
.coach h3{font-size:16px;font-weight:700;color:var(--ink)}
.coach .email{color:var(--blue);font-size:11.5px}
.coach p{font-size:11.5px;line-height:1.55;padding:16px 40px 0}
.slider-arrow{position:absolute;top:300px}
.slider-arrow.prev{left:-68px}.slider-arrow.next{right:-68px}

/* footer */
.site-footer{height:263px;background:var(--footer);color:#ddd}
.site-footer .wrap{display:flex;padding-top:52px}
.footer-brand{width:372px}
.footer-brand .brand{font-size:20px;margin-bottom:20px}
.footer-item{display:flex;gap:12px;align-items:flex-start;font-size:11.5px;line-height:1.5;margin-bottom:14px}
.footer-item a{color:var(--blue);text-decoration:none}
.quick-links{width:200px}
.site-footer h5{font-size:13px;font-weight:700;color:var(--white);margin-bottom:10px}
.quick-links ul{list-style:none;font-size:12px}
.quick-links li::before{content:"• ";color:var(--white)}
.quick-links li:first-child a{color:var(--orange)}
.quick-links a{color:#ddd;text-decoration:none}
.social-box{width:176px;height:146px;background:var(--white);padding:8px;color:#333;font-size:10px;line-height:1.35}
.social-box .head{display:flex;gap:8px;background:#3a3a3a;color:var(--white);padding:6px;height:50px}
.social-box .head .sq{width:36px;height:36px;background:#555}
.social-box .head strong{font-size:11px;display:block}
.social-box .like{display:inline-block;background:#eee;border:1px solid #ccc;padding:0 5px;color:#333;font-size:9px;margin-top:2px}
.social-box .friends{display:flex;gap:4px;margin-top:6px}
.social-box .friends span{width:22px;height:22px;background:#ccc}
.copyright{height:52px;background:var(--footer-deep);color:#aaa;font-size:11px}
.copyright .wrap{line-height:52px}
</style>
</head>
<body>

<header>
  <div class="topbar">
    <div class="wrap">
      <div class="brand"><span class="mark"></span>Kelbro Studio</div>
      <nav class="main-nav">
        <a href="#" class="active">Home</a>
        <a href="#">About Us</a>
        <a href="#">Packages</a>
        <a href="#">Coaches</a>
        <a href="#">Testimonials</a>
        <a href="#">Contact Us</a>
      </nav>
    </div>
  </div>
  <div class="hero-photo" role="img" aria-label="Portrait photo of the two coaches standing together in suits"></div>
  <div class="hero-band">
    <div class="wrap">
      <h1>Lorem Ipsum has been the industry's dummy standard dummy text ever</h1>
      <a href="#" class="btn-outline">Book Now</a>
    </div>
  </div>
</header>

<section class="intro">
  <div class="wrap">
    <h2 class="section-title">One step that can change your life</h2>
    <p>Lifestyle Coaching is about finding out what creates a highly prosperous and high freedom in your life. It's about finding out what you really want with your life and then step by step to design a lifestyle around all this. A life-style that will last a lifetime and not...</p>
    <a href="#" class="btn-outline">Read More</a>
  </div>
</section>

<section class="lifestyle">
  <div class="wrap">
    <div class="matrix-art" role="img" aria-label="Vardagskartan lifestyle matrix illustration with four coloured quadrants and axis arrows"></div>
    <div class="lifestyle-copy">
      <h3>What is a richer lifestyle?</h3>
      <p>What is a richer lifestyle may differ between different people. It can also be quite difficult on their own to get a good picture of what you really mean by this.</p>
      <p>We have therefore developed a simple model to facilitate the under-standing and the creation of a richer lifestyle. This is a model we call Vardagskartan and consists of the following four parts representing respective lifestyle.</p>
      <a href="#" class="btn-outline">Read More</a>
    </div>
  </div>
</section>

<section class="why">
  <div class="wrap">
    <h2 class="section-title">Why Choose Coaching?</h2>
    <div class="usp-row">
      <div class="usp"><div class="label">Commitment</div><div class="num">01</div><p>Everyone can set goals, but not everyone has the ability to pursue.</p></div>
      <div class="usp featured"><div class="label">Challenging</div><div class="num">02</div><p>We will help you to get outside your comfortzone. It is outside the...</p></div>
      <div class="usp"><div class="label">Support</div><div class="num">03</div><p>All we sometimes need support, especially in the quest to create.</p></div>
      <div class="usp"><div class="label">You are unique</div><div class="num">04</div><p>There is no 'one-fits-all' solution. Everyone is different with.</p></div>
    </div>
  </div>
</section>

<section class="covering">
  <div class="wrap">
    <h2 class="section-title">We Are Covering Coaching Session</h2>
    <h4>How does it work?</h4>
    <p>Together with your coach you will develop a tailored approach that is appropriate for your circumstances and ambitions. This is because we humans are in different phases of life. Some need more time to find out what they really want to live the lifestyle while others have different obstacles in their path they need to address in order to achieve the results they want. There are many areas to focus on, depending on where you are in life.</p>
    <p class="lead">These are examples of different areas that your coach will go through with you.</p>
    <ul class="ticks">
      <li><svg width="12" height="12" viewBox="0 0 12 12"><rect width="12" height="12" rx="2" fill="#fbb03b"/><path d="M3 6.2l2 2 4-4.4" stroke="#fff" stroke-width="1.6" fill="none"/></svg>Where are you right now in the life-style array?</li>
      <li><svg width="12" height="12" viewBox="0 0 12 12"><rect width="12" height="12" rx="2" fill="#fbb03b"/><path d="M3 6.2l2 2 4-4.4" stroke="#fff" stroke-width="1.6" fill="none"/></svg>Where do you want to be in life-style array?</li>
      <li><svg width="12" height="12" viewBox="0 0 12 12"><rect width="12" height="12" rx="2" fill="#fbb03b"/><path d="M3 6.2l2 2 4-4.4" stroke="#fff" stroke-width="1.6" fill="none"/></svg>Find a route that suits you and you seem to think is fun.</li>
      <li><svg width="12" height="12" viewBox="0 0 12 12"><rect width="12" height="12" rx="2" fill="#fbb03b"/><path d="M3 6.2l2 2 4-4.4" stroke="#fff" stroke-width="1.6" fill="none"/></svg>Getting Started, or build your own money machine</li>
      <li><svg width="12" height="12" viewBox="0 0 12 12"><rect width="12" height="12" rx="2" fill="#fbb03b"/><path d="M3 6.2l2 2 4-4.4" stroke="#fff" stroke-width="1.6" fill="none"/></svg>Break down big goals into manageable sub-goals</li>
      <li><svg width="12" height="12" viewBox="0 0 12 12"><rect width="12" height="12" rx="2" fill="#fbb03b"/><path d="M3 6.2l2 2 4-4.4" stroke="#fff" stroke-width="1.6" fill="none"/></svg>Continuously check that you are on track and making progress</li>
    </ul>
    <div class="divider"></div>
    <div class="prep">
      <div><h4>What do I need?</h4><p>The call is implemented via the program Talkio.<br>All you need is a computer and a headset, alternatively,<br>a microphone and speakers.</p></div>
      <div><h4>How do I book coaching?</h4><p>Select a single session or one of our packages. Write what times of day that suits you best. We will contact you then to find a time that suits us both.</p></div>
    </div>
  </div>
</section>

<section class="packages" role="region" aria-label="Packages over a background photo of coins and a pen">
  <div class="wrap">
    <h2 class="section-title">Invest in Your Self</h2>
    <p class="intro-text">You want something you do not already have? Start when designing a lifestyle you have not previously lived. We, at Kelbro Studio will help you with this by lifestyle coaching. Below, you can choose one of our coaching packages.</p>
    <div class="package-row">
      <div class="package bronze"><div class="medal" role="img" aria-label="Bronze medal graphic"></div><div class="band">Disposable Session</div><div class="details">Includes 1 session Price<br><strong>650 SEK</strong></div><a href="#" class="btn">Book Now</a></div>
      <div class="package silver"><div class="medal" role="img" aria-label="Silver medal graphic"></div><div class="band">Silver Package</div><div class="details">Includes 3 sessions Price<br><strong>3050 SEK</strong></div><a href="#" class="btn">Book Now</a></div>
      <div class="package gold"><div class="medal" role="img" aria-label="Gold medal graphic"></div><div class="band">Gold Package</div><div class="details">Includes 10 sessions Price<br><strong>5800 SEK</strong></div><a href="#" class="btn">Book Now</a></div>
    </div>
  </div>
</section>

<section class="testimonials">
  <div class="wrap">
    <h2 class="section-title">Testimonials</h2>
    <div class="quote-mark">&ldquo;</div>
    <blockquote>" Refreshing and inspiring! Comes with simple everyday tips as well as harder tips. A fun way to get a kick in the butt, so that the economy-energy stays! Thanks for a great conversation! "</blockquote>
    <cite>Annelie Brunstedt</cite>
    <div class="dots"><span class="on"></span><span></span></div>
  </div>
</section>

<section class="coaches">
  <div class="wrap">
    <h2 class="section-title">We as coaches</h2>
    <svg class="slider-arrow prev" width="14" height="24" viewBox="0 0 14 24"><path d="M12 2L3 12l9 10" stroke="#aaa" stroke-width="2" fill="none"/></svg>
    <svg class="slider-arrow next" width="14" height="24" viewBox="0 0 14 24"><path d="M2 2l9 10-9 10" stroke="#aaa" stroke-width="2" fill="none"/></svg>
    <div class="coach-row">
      <div class="coach">
        <div class="portrait" role="img" aria-label="Portrait photo of coach Henrik Sandelin" style="background:radial-gradient(circle,#6b5a4c,#2d2620)"></div>
        <h3>Henrik Sandelin</h3>
        <div class="email">henrik@kelbrostudio.se</div>
        <p>Versatile investors with a focus on alternative and high risk investments. Besides the stock market, investing in unlisted startup companies and various Internet-based investments such as P2P lending, online games and apps.</p>
      </div>
      <div class="coach">
        <div class="portrait" role="img" aria-label="Portrait photo of coach Tobias Lindqvist" style="background:radial-gradient(circle,#d8c3a8,#6d8b5a)"></div>
        <h3>Tobias Lindqvist</h3>
        <div class="email">tobias@kelbrostudio.se</div>
        <p>Tobias has a broad background in finance and IT. As an investor is his focus on dividend stocks, real estate and Internet-based entrepreneurship. He also has a long experience and a passion to help people and businesses to evolve in different ways...</p>
      </div>
    </div>
  </div>
</section>

<footer class="site-footer">
  <div class="wrap">
    <div class="footer-brand">
      <div class="brand"><span class="mark"></span>Kelbro Studio</div>
      <div class="footer-item">
        <svg width="16" height="22" viewBox="0 0 16 22"><path d="M8 0a8 8 0 0 0-8 8c0 6 8 14 8 14s8-8 8-14a8 8 0 0 0-8-8z" fill="#29a8e0"/><circle cx="8" cy="8" r="3" fill="#333"/></svg>
        <span>Kelbro Studio AB Lindvägen 12<br>412 50 Göteborg</span>
      </div>
      <div class="footer-item">
        <svg width="16" height="22" viewBox="0 0 16 22"><circle cx="8" cy="11" r="8" fill="#29a8e0"/><text x="8" y="15" text-anchor="middle" font-size="11" font-weight="700" fill="#333" font-family="Open Sans,sans-serif">?</text></svg>
        <span>For Questions, Contact Us At<br><a href="#">team@kelbrostudio.se</a></span>
      </div>
    </div>
    <div class="quick-links">
      <h5>Quick Links</h5>
      <ul><li><a href="#">Blogg</a></li><li><a href="#">Coaching</a></li><li><a href="#">Om oss</a></li></ul>
    </div>
    <div>
      <h5>Follow Us On Social</h5>
      <div class="social-box">
        <div class="head"><span class="sq"></span><div><strong>Kelbro Studio</strong><span class="like">Like Page</span></div></div>
        <p style="margin-top:6px">Be the first of your friends to like this</p>
        <div class="friends"><span></span><span></span><span></span></div>
      </div>
    </div>
  </div>
</footer>
<div class="copyright"><div class="wrap">Copyright 2016 Kelbro Studio AB</div></div>

</body>
</html>
```